I am looking for a whole Stationery Design for my Company. A new Logo, Letterhead and Business Card. I have attached an old Logo which looks very bad. Be creative and use your own ideas for the Logo as well as all other designs.

```html
<!DOCTYPE html>
<html lang="en">
<head>
<meta charset="utf-8">
<title>Tlhapane Projects Letterhead</title>
<link rel="stylesheet" href="https://fonts.googleapis.com/css2?family=Open+Sans:wght@400;800&display=swap">
<style>
  :root {
    --brand-blue: #184682;
    --brand-grey: #9e9e9e;
    --paper: #fdfdfd;
    --backdrop: #ffffff;
    --ink: #333333;
  }
  html, body {
    margin: 0;
    padding: 0;
    width: 1200px;
    height: 1200px;
    overflow: hidden;
    background: var(--backdrop);
  }
  .letterhead {
    position: absolute;
    left: 228px;
    top: 72px;
    width: 745px;
    height: 1056px;
    background: var(--paper);
    box-shadow: 0 0 8px rgba(0,0,0,0.25);
    overflow: hidden;
    font-family: "Open Sans", Arial, sans-serif;
  }
  .letterhead__art {
    position: absolute;
    left: 0;
    top: 0;
    width: 745px;
    height: 1056px;
  }
  .brand-name {
    position: absolute;
    left: 50px;
    top: 70px;
    margin: 0;
    font-size: 31px;
    font-weight: 800;
    color: var(--brand-blue);
    letter-spacing: 0.5px;
    line-height: 1;
  }
  .contact-block {
    position: absolute;
    left: 52px;
    top: 956px;
    margin: 0;
    font-size: 11.5px;
    line-height: 15.5px;
    color: var(--ink);
    font-style: normal;
  }
  .contact-block span { display: block; }
  .contact-block .address { padding-left: 2px; }
</style>
</head>
<body>
  <main class="letterhead">
    <svg class="letterhead__art" viewBox="0 0 745 1056" aria-hidden="true">
      <!-- header bands -->
      <path class="header-grey" d="M300 0 H745 V54 H375 Q360 54 350 46 Z" fill="var(--brand-grey)"/>
      <path class="header-blue" d="M476 0 H745 V46 H526 Q516 46 510 40 Z" fill="var(--brand-blue)"/>
      <!-- footer bands -->
      <path class="footer-grey" d="M514 982 H743 V1028 H474 Z" fill="var(--brand-grey)"/>
      <rect class="footer-blue" x="2" y="1028" width="743" height="28" fill="var(--brand-blue)"/>
    </svg>

    <h1 class="brand-name">Tlhapane Projects</h1>

    <address class="contact-block">
      <span class="address">address address address address</span>
      <span class="tel">tel no : 000 000 000 000 \</span>
      <span class="mail">mail&nbsp;&nbsp;&nbsp; : xxxxxxxxx@xxxx.com</span>
      <span class="web">web&nbsp;&nbsp;&nbsp; : xxxxxxxxxxx.com</span>
    </address>
  </main>
</body>
</html>
```